Kestwell Finanz AG needs web design

We need a website for a Swiss company: Kestwell Finanz AG. We offer our customers financial services such as advice and funds. We also have an interest rate calculator that we want to link to via a button on the website.

We are looking for a black and gold design. (Background: Black, Accents: Gold and White)
The design should convey security and growth. We have uploaded our logo in the attachment.
Font from the logo: Trajan Pro Regular

```html
<!DOCTYPE html>
<html lang="en">
<head>
<meta charset="utf-8">
<title>Kestwell Finanz AG</title>
<link href="https://fonts.googleapis.com/css2?family=Cinzel:wght@400;600&family=Poppins:wght@300;400&display=swap" rel="stylesheet">
<style>
:root{
  --black:#000;
  --charcoal:#232323;
  --gold:#c6a768;
  --gold-light:#ecd8a6;
  --gold-deep:#a8894d;
  --gold-panel:#b59a5e;
  --white:#fff;
  --paper:#f1f1f1;
  --ink:#222;
  --muted:#d9d9d9;
}
*{margin:0;padding:0;box-sizing:border-box}
html,body{width:1200px;height:4267px;overflow:hidden}
body{position:relative;background:var(--charcoal);font-family:"Poppins",sans-serif;color:var(--white)}
.abs{position:absolute}
.serif{font-family:"Cinzel",serif}
.gold-btn{position:absolute;display:flex;align-items:center;justify-content:center;border-radius:26px;
  background:linear-gradient(180deg,var(--gold-light),var(--gold-deep));color:var(--ink);
  font-family:"Cinzel",serif;font-size:15px;letter-spacing:.5px;text-decoration:none}
.dark-btn{background:var(--black);color:var(--white)}
.photo{position:absolute}
.lede{font-size:13.5px;line-height:19.5px;font-weight:300}
.section-title{position:absolute;font-family:"Cinzel",serif;font-weight:400;color:var(--gold);letter-spacing:1px}
.rule{position:absolute;height:3px;background:linear-gradient(90deg,var(--gold-light),var(--gold-deep))}
.brand{position:absolute;font-family:"Cinzel",serif;color:var(--gold);text-align:center;line-height:1.15}
.brand .mark{display:block;width:46px;height:46px;border-radius:50%;background:var(--gold);margin:0 auto 10px}

/* hero */
.hero{left:0;top:0;width:1200px;height:746px;background:linear-gradient(120deg,#3a3833 0%,#4b4538 45%,#2c2c30 80%,#3b4556 100%)}
.hero-shade{left:0;top:0;width:1200px;height:746px;background:linear-gradient(180deg,rgba(0,0,0,.75) 0%,rgba(0,0,0,.35) 40%,rgba(0,0,0,.5) 100%)}
.nav{top:112px;left:0;width:1200px;font-family:"Cinzel",serif;font-size:15px}
.nav a{position:absolute;color:var(--gold-light);text-decoration:none}
.nav a.current{color:var(--white)}
.welcome{top:258px;width:1200px;text-align:center;font-family:"Cinzel",serif;color:var(--gold);font-size:31px}
.hero-title{top:315px;width:1200px;text-align:center;font-family:"Cinzel",serif;color:var(--gold-light);font-size:58px;line-height:64px}

/* services */
.services{left:0;top:1304px;width:1200px;height:557px;background:var(--black)}
.service{position:absolute;top:193px;width:170px;text-align:center}
.service svg{display:block;margin:0 auto 14px}
.service p{font-family:"Cinzel",serif;font-size:14px;line-height:19px;color:var(--gold)}
.service.active p{color:var(--white)}

/* team */
.team-card{left:73px;top:1967px;width:613px;height:457px;background:var(--paper)}
.team-side{left:1090px;top:1967px;width:110px;height:457px;background:#ececec}
.tab{left:1128px;top:2126px;width:48px;height:185px;border-radius:24px;background:linear-gradient(90deg,var(--gold-light),var(--gold-deep));
  display:flex;align-items:center;justify-content:center}
.tab span{transform:rotate(-90deg);white-space:nowrap;font-family:"Cinzel",serif;font-size:14px;color:var(--ink)}

/* news */
.card{position:absolute;top:3223px;width:280px;height:378px;background:var(--paper)}
.card .photo{left:0;top:0;width:280px;height:204px}
.card .date{position:absolute;left:28px;top:225px;font-family:"Cinzel",serif;font-size:10px;color:#999}
.card h3{position:absolute;left:28px;top:248px;width:230px;font-family:"Cinzel",serif;font-weight:400;font-size:15px;line-height:20px;color:var(--ink)}
.card .gold-btn{left:28px;top:318px;width:120px;height:38px;font-size:13px}

/* footer */
.contact-row{position:absolute;left:154px;display:flex;align-items:center;gap:18px;font-size:16px;line-height:21px}
.contact-row .ico{width:38px;height:38px;border-radius:50%;background:linear-gradient(180deg,var(--gold-light),var(--gold-deep));display:flex;align-items:center;justify-content:center}
.foot-nav{left:474px;top:3955px;font-family:"Cinzel",serif;font-size:13px;line-height:28px}
.foot-nav a{display:block;color:var(--gold);text-decoration:none}
.foot-nav a:first-child{color:var(--white)}
.legal{left:150px;top:4148px;font-family:"Cinzel",serif;font-size:12.5px;line-height:25px}
.field{position:absolute;color:var(--ink);font-size:15px;border-bottom:1px solid #8a7a55;height:32px}
.social{position:absolute;top:4177px;width:26px;height:26px;border-radius:50%;background:var(--black)}
</style>
</head>
<body>

<!-- HERO -->
<header>
  <div class="abs hero" role="img" aria-label="Photo of an advisor with a clipboard talking with an elderly couple in a bright living room"></div>
  <div class="abs hero-shade"></div>
  <div class="brand" style="left:130px;top:30px;width:260px;font-size:22px"><span class="mark"></span>Kestwell Finanz AG</div>
  <a class="gold-btn" href="#calculator" style="left:759px;top:33px;width:290px;height:46px;font-size:15px">Interest Rate Calculator</a>
  <nav class="abs nav">
    <a class="current" href="#" style="left:431px">Home</a>
    <a href="#services" style="left:524px">Services</a>
    <a href="#about" style="left:641px">About</a>
    <a href="#news" style="left:744px">News</a>
    <a href="#" style="left:833px">Customers</a>
    <a href="#contact" style="left:974px">Contact</a>
  </nav>
  <p class="abs welcome">Welcome to</p>
  <h1 class="abs hero-title">Kestwell Finanz<br>AG</h1>
  <div class="rule" style="left:352px;top:406px;width:185px;height:3px"></div>
  <div class="rule" style="left:663px;top:406px;width:185px;height:3px"></div>
</header>

<!-- ABOUT -->
<section id="about">
  <div class="photo" style="left:141px;top:855px;width:416px;height:371px;border-radius:26px 0 26px 0;border-left:4px solid var(--gold);border-bottom:4px solid var(--gold);background:linear-gradient(135deg,#d9d5cc,#7b8790 55%,#3a3f46)" role="img" aria-label="Photo of three colleagues reviewing documents and a laptop at a table"></div>
  <h2 class="section-title" style="left:631px;top:868px;font-size:40px">About Us</h2>
  <div class="rule" style="left:641px;top:930px;width:155px"></div>
  <p class="abs lede" style="left:641px;top:958px;width:445px">Lorem ipsum dolor sit amet, consectetur adipiscing elit, sed do eiusmod tempor incididunt ut labore et dolore magna aliquauis ipsum suspendisse ultrices gravida. Risus commodo viverra ma ecenas accumsan lacus vel facilisisorem ipsum dolor sit amet, consectetur adipiscing elit, sed do eiusmod tempor incididunt ut labore et dolore magna aliquauis ipsum suspendisse ultrices gravida. Risus commodo viverra maecenas accumsan lacus vel facilisismagna aliquauis ipsum sus.</p>
  <a class="gold-btn" href="#" style="left:631px;top:1152px;width:141px;height:46px">Read More</a>
</section>

<!-- SERVICES -->
<section id="services" class="abs services">
  <h2 class="section-title" style="left:0;top:82px;width:1200px;text-align:center;font-size:40px">Our Services</h2>
  <div class="service active" style="left:129px">
    <svg width="70" height="74" viewBox="0 0 70 74" fill="none" stroke="var(--gold)" stroke-width="2"><path d="M35 12a18 18 0 0 0-11 32c3 3 4 6 4 10h14c0-4 1-7 4-10a18 18 0 0 0-11-32z"/><path d="M28 60h14M29 65h12M32 70h6M35 2v5M14 10l4 4M56 10l-4 4M6 30h5M59 30h5M30 54V36l5 5 5-5v18"/></svg>
    <p>Lorem ipsum<br>dolor sit amet</p>
  </div>
  <div class="service" style="left:321px">
    <svg width="70" height="74" viewBox="0 0 70 74" fill="none" stroke="var(--gold)" stroke-width="2"><rect x="24" y="6" width="38" height="28" rx="3"/><circle cx="34" cy="17" r="5"/><path d="M43 14h13M43 20h13M30 27h26M4 50l12-8h16l8 6H28M4 66l8-5h22l22-14c3-2 6 2 3 5L36 70H10"/></svg>
    <p>Lorem ipsum<br>dolor sit amet</p>
  </div>
  <div class="service" style="left:513px">
    <svg width="70" height="74" viewBox="0 0 70 74" fill="none" stroke="var(--gold)" stroke-width="2"><circle cx="38" cy="20" r="16"/><path d="M43 13c-2-3-10-3-10 2s10 3 10 9-8 5-10 2M38 8v4M38 29v4M4 50l12-8h16l8 6H28M4 66l8-5h22l22-14c3-2 6 2 3 5L36 70H10"/></svg>
    <p>Lorem ipsum<br>dolor sit amet</p>
  </div>
  <div class="service" style="left:705px">
    <svg width="70" height="74" viewBox="0 0 70 74" fill="none" stroke="var(--gold)" stroke-width="2"><path d="M30 20l-5-12 10 4 10-4-5 12M30 20h10M30 20C18 30 16 42 20 52M40 20c12 10 14 22 10 32"/><circle cx="44" cy="50" r="14"/><path d="M48 44c-2-2-8-2-8 1s8 3 8 7-6 4-8 2M44 40v3M44 57v3"/><path d="M6 56h16v6H6zM8 62h16v6H8zM6 68h18v4H6z"/></svg>
    <p>Lorem ipsum<br>dolor sit amet</p>
  </div>
  <div class="service" style="left:898px">
    <svg width="70" height="74" viewBox="0 0 70 74" fill="none" stroke="var(--gold)" stroke-width="2"><path d="M18 4h34l10 10v56H18z"/><path d="M52 4v10h10"/><circle cx="14" cy="20" r="10"/><path d="M14 10v10h10M26 56l10-12 8 8 12-14M24 26h20M30 32h14"/></svg>
    <p>Lorem ipsum<br>dolor sit amet</p>
  </div>
  <p class="abs lede" style="left:170px;top:420px;width:860px;text-align:center;color:var(--muted);font-size:13px">Lorem ipsum dolor sit amet, consectetur adipiscing elit, sed do eiusmod tempor incididunt ut labore et dolore magna aliquauis ipsum suspendisse ultrices gravida. Risus commodo viverra mecenas accumsan lacus vel facilisisorem ipsum dolor sit amet, consectetur adipiscing elit, sed do eiusmod tempor incididuntut labore et dolore magna aliquauis ipsum suspe</p>
</section>

<!-- TEAM -->
<section id="team">
  <div class="abs team-card"></div>
  <div class="abs team-side"></div>
  <div class="photo" style="left:686px;top:1967px;width:404px;height:457px;background:linear-gradient(160deg,#d8cbb4,#a38a6a 50%,#4a4440)" role="img" aria-label="Photo of a team gathered around a laptop in an office"></div>
  <h2 class="section-title" style="left:146px;top:2035px;font-size:44px">Meet Our Team</h2>
  <div class="rule" style="left:146px;top:2096px;width:155px"></div>
  <p class="abs lede" style="left:146px;top:2130px;width:445px;color:var(--ink)">Lorem ipsum dolor sit amet, consectetur adipiscing elit, sed do eiusmod tempor incididunt ut labore et dolore magna aliquauis ipsum suspendisse ultrices gravida. Risus commodo viverra ma ecenas accumsan lacus vel facilisisorem ipsum dolor sit amet, consectetur adipiscing elit, sed do eiusmod tempor incididunt ut labore et dolore magna aliquauis ipsum suspendisse ultrices gravida. Risus commodo viverra maecenas accumsan lacus vel facilisismagna aliquauis ipsum sus.</p>
  <a class="gold-btn" href="#" style="left:146px;top:2321px;width:141px;height:46px">Read More</a>
  <div class="abs tab"><span>Meet Our Team</span></div>
</section>

<!-- VISION -->
<section id="vision">
  <div class="photo" style="left:0;top:2547px;width:636px;height:472px;background:linear-gradient(135deg,#c9c4b8,#6f7b8c 45%,#2c3446 75%,#b98d5c)" role="img" aria-label="Photo of business people shaking hands across a meeting table"></div>
  <div class="abs" style="left:636px;top:2547px;width:564px;height:472px;background:var(--gold-panel)"></div>
  <h2 class="section-title" style="left:694px;top:2640px;font-size:42px;color:var(--white)">Our Vision</h2>
  <p class="abs lede" style="left:694px;top:2718px;width:445px">Lorem ipsum dolor sit amet, consectetur adipiscing elit, sed do eiusmod tempor incididunt ut labore et dolore magna aliquauis ipsum suspendisse ultrices gravida. Risus commodo viverra ma ecenas accumsan lacus vel facilisisorem ipsum dolor sit amet, consectetur adipiscing elit, sed do eiusmod tempor incididunt ut labore et dolore magna aliquauis ipsum suspendisse ultrices gravida. Risus commodo viverra maecenas accumsan lacus vel facilisismagna aliquauis ipsum sus.</p>
  <a class="gold-btn dark-btn" href="#" style="left:694px;top:2910px;width:141px;height:46px">Read More</a>
</section>

<!-- NEWS -->
<section id="news">
  <h2 class="section-title" style="left:0;top:3110px;width:1200px;text-align:center;font-size:42px">Latest News</h2>
  <div class="rule" style="left:398px;top:3176px;width:170px"></div>
  <div class="rule" style="left:583px;top:3176px;width:170px"></div>
  <article class="card" style="left:151px">
    <div class="photo" style="background:linear-gradient(135deg,#e8e2d8,#9a8f83 55%,#4a4a4a)" role="img" aria-label="Photo of two smiling business colleagues"></div>
    <span class="date">Mar 01 2022</span>
    <h3>Lorem ipsum dolor sit amet, consectetur adipiscing elit</h3>
    <a class="gold-btn" href="#">Read More</a>
  </article>
  <article class="card" style="left:459px">
    <div class="photo" style="background:linear-gradient(135deg,#4a4a4a,#c9cdd2 50%,#7fa2c9)" role="img" aria-label="Photo of hands reviewing charts on paper with a pen"></div>
    <span class="date">Mar 01 2022</span>
    <h3>Lorem ipsum dolor sit amet, consectetur adipiscing elit</h3>
    <a class="gold-btn" href="#">Read More</a>
  </article>
  <article class="card" style="left:767px">
    <div class="photo" style="background:linear-gradient(135deg,#0f1f3a,#2e6f9e 50%,#9cc6e8)" role="img" aria-label="Photo of a hand in front of digital financial dashboards"></div>
    <span class="date">Mar 01 2022</span>
    <h3>Lorem ipsum dolor sit amet, consectetur adipiscing elit</h3>
    <a class="gold-btn" href="#">Read More</a>
  </article>
</section>

<!-- FOOTER -->
<footer id="contact">
  <svg class="abs" style="left:0;top:3690px" width="1200" height="577" viewBox="0 0 1200 577">
    <polygon points="0,0 1200,95 1200,577 0,577" fill="var(--black)"/>
    <defs><linearGradient id="formGold" x1="0" y1="0" x2="0" y2="1"><stop offset="0" stop-color="#ecd8a6"/><stop offset="1" stop-color="#c3a56a"/></linearGradient></defs>
    <polygon points="664,95 1122,120 1122,577 664,577" fill="url(#formGold)"/>
  </svg>
  <div class="brand" style="left:140px;top:3768px;width:285px;font-size:26px"><span class="mark"></span>Kestwell Finanz AG</div>

  <div class="contact-row" style="top:3949px">
    <span class="ico"><svg width="18" height="18" viewBox="0 0 24 24" fill="var(--ink)"><path d="M6.6 10.8a15 15 0 0 0 6.6 6.6l2.2-2.2c.3-.3.7-.4 1-.2 1.1.4 2.3.6 3.6.6.6 0 1 .4 1 1V20c0 .6-.4 1-1 1A17 17 0 0 1 3 4c0-.6.4-1 1-1h3.5c.6 0 1 .4 1 1 0 1.3.2 2.5.6 3.6.1.3 0 .7-.2 1z"/></svg></span>
    <span>Phone<br>+41 44 310 5270</span>
  </div>
  <div class="contact-row" style="top:4003px">
    <span class="ico"><svg width="18" height="14" viewBox="0 0 24 18" fill="none" stroke="var(--ink)" stroke-width="2"><rect x="1" y="1" width="22" height="16" rx="2"/><path d="M1 2l11 8 11-8"/></svg></span>
    <span>Email<br>info@kestwell-finanz.ch</span>
  </div>
  <div class="contact-row" style="top:4068px">
    <span class="ico"><svg width="14" height="18" viewBox="0 0 16 22" fill="var(--ink)"><path d="M8 0a8 8 0 0 0-8 8c0 6 8 14 8 14s8-8 8-14a8 8 0 0 0-8-8zm0 11a3 3 0 1 1 0-6 3 3 0 0 1 0 6z"/></svg></span>
    <span>Talstrasse 48<br>8001 Zürich</span>
  </div>

  <nav class="abs foot-nav">
    <a href="#">Home</a><a href="#services">Services</a><a href="#about">About</a><a href="#news">News</a><a href="#">Customers</a><a href="#contact">Contact</a>
  </nav>
  <p class="abs legal">© 2022 All Rights Reserved.<br>Terms &amp; Conditions Privacy Policy</p>

  <form>
    <div class="field" style="left:737px;top:3903px;width:317px">Name:</div>
    <div class="field" style="left:737px;top:3953px;width:317px">Email:</div>
    <div class="field" style="left:737px;top:4003px;width:148px">Phone:</div>
    <div class="field" style="left:906px;top:4003px;width:148px">Subject:</div>
    <div class="field" style="left:737px;top:4053px;width:317px;height:86px">Message:</div>
    <a class="gold-btn dark-btn" href="#" style="left:731px;top:4171px;width:144px;height:48px;font-size:21px;border-radius:26px;color:var(--gold-light)">Submit</a>
  </form>
  <span class="social" style="left:903px"></span>
  <span class="social" style="left:946px"></span>
  <span class="social" style="left:984px"></span>
</footer>

</body>
</html>
```